We need a web design for a retail food business based in Greater Western Sydney Australia called Golden Lantern Chinese Restaurant. Basically just need a simple yet easily to navigate website to browse through a menu, gallery , brief description about us, opening hours.
Menu and Gallery will be constantly updated.
Will provide own images for gallery
Updates
Menu has been uploaded and some idea on the colours I would like on the site
Some additional pictures added to see what designs you guys can come up with . Thanks again
To All Designers,
Any extra fee on top of the designs that feels need to be charged, please let me know in advance
Reason: Extending Deadline as I have yet to find a design that I would like...Thanks guys
Target Market(s)
All groups
Industry/Entity Type
Business
Requirements
Must have
- Open minded to any designs
Nice to have
- Would like slideshow behind main logo.
Preferred light coloured site yet not too playful
Should not have
- Preferably no dark colours backgrounds

```html
<!DOCTYPE html>
<html lang="en">
<head>
<meta charset="utf-8">
<title>Golden Lantern Chinese Restaurant – Contact Us</title>
<link rel="stylesheet" href="https://fonts.googleapis.com/css2?family=Titillium+Web:wght@400;600&family=Roboto+Condensed:wght@400;700&display=swap">
<style>
:root{
  --red-dark:#c0252a;
  --red:#e5433f;
  --red-soft:#f0a7a0;
  --pink-line:#f6c9c0;
  --grey-line:#c9c9c9;
  --charcoal:#3b3638;
  --gold:#f2df8a;
  --panel:#e9e9e9;
  --ink:#1b1b1b;
  --white:#ffffff;
}
*{box-sizing:border-box;margin:0;padding:0}
html,body{width:1043px;height:1200px;overflow:hidden;background:var(--white)}
body{position:relative;font-family:"Roboto Condensed",Arial,sans-serif;color:var(--ink)}
.abs{position:absolute;white-space:nowrap}

.topbar{left:0;top:0;width:1043px;height:29px;background:var(--red-dark);color:var(--white);font-size:14px}
.topbar .call{position:absolute;left:140px;top:6px;display:flex;align-items:center;gap:6px}
.brandband{left:0;top:29px;width:1043px;height:72px;background:var(--red)}
.brand{left:323px;top:40px;width:397px;height:130px;display:flex;align-items:center;justify-content:center;gap:14px}
.brand .mark{width:54px;height:54px;border-radius:50%;background:var(--red-dark)}
.brand .name{font-family:"Titillium Web",sans-serif;font-weight:600;font-size:30px;line-height:1.05;color:var(--red-dark);background:var(--white);padding:6px 10px}

.mainnav{left:0;top:180px;width:1043px;height:24px;font-size:18px;color:var(--ink)}
.mainnav a{position:absolute;top:0;color:inherit;text-decoration:none}
.rule{left:0;width:1043px}
.rule.grey{top:205px;height:4px;background:var(--grey-line)}
.rule.pink1{top:212px;height:3px;background:var(--pink-line)}
.rule.pink2{top:349px;height:3px;background:var(--pink-line)}
.rule.pink3{top:356px;height:3px;background:var(--red-soft)}

.hero{left:0;top:220px;width:1043px;height:127px;background:linear-gradient(90deg,#d9b441 0%,#b88a2e 30%,#8a6a2c 55%,#c9762e 85%,#e0622a 100%)}
.hero-shade{left:219px;top:220px;width:615px;height:127px;background:rgba(40,25,15,.55)}
.hero-title{left:231px;top:252px;font-family:"Titillium Web",sans-serif;font-weight:600;font-size:43px;line-height:1;color:var(--gold);border-bottom:2px solid var(--gold);padding-bottom:2px}

.content{left:0;top:363px;width:1043px;height:748px;background:var(--charcoal)}

.map{left:212px;top:415px;width:394px;height:170px;border:2px solid var(--gold);background:linear-gradient(135deg,#e6e1d3,#d7dcc8 50%,#cfd8e2)}
.address{left:212px;top:594px;width:394px;text-align:center;font-family:"Titillium Web",sans-serif;font-size:17.5px;line-height:27px;color:var(--gold)}
.divider{left:212px;top:652px;width:394px;height:14px}
.callout{left:216px;top:681px;width:400px;font-family:"Titillium Web",sans-serif;font-size:16px;line-height:20px;color:#eee}
.callout .phone{color:var(--gold)}

.label{left:215px;font-family:"Titillium Web",sans-serif;font-size:13px;color:#eee}
.field{left:214px;background:var(--white);border:2px solid #cfcfcf}
.submit{left:214px;top:1057px;width:56px;height:22px;background:var(--red);color:var(--white);font-family:"Titillium Web",sans-serif;font-size:14px;text-align:center;line-height:22px}

.side{left:634px;top:417px;width:194px;height:488px;background:var(--panel)}
.side-head{left:637px;width:188px;height:29px;background:var(--red);border-left:5px solid #222;color:var(--white);font-family:"Titillium Web",sans-serif;font-size:16px;line-height:29px;padding-left:8px}
.meal{left:640px;font-size:14px;text-decoration:underline;color:var(--ink)}
.hours-row{left:640px;width:184px;height:22px;font-size:12px;display:flex;align-items:center;border-bottom:1px solid #d3d6e6;color:#333}
.hours-row .day{width:76px;flex:none}
.hours-row .time{display:flex;align-items:center;gap:5px;flex:none}
.hours-row svg{flex:none}
.hours-row.lunch .day{width:96px;font-size:12.5px;color:#111}
.dash{left:642px;top:730px;width:176px;border-top:1px dashed #7a7fc0}
.recipe{left:651px;font-size:12.5px;letter-spacing:.3px;color:#222}
.recipe::before{content:"›";color:var(--red);font-weight:700;margin-right:5px}

.tab{left:0;width:94px;background:linear-gradient(#ee5a55,#d83a36);color:var(--white);font-family:Arial,sans-serif;font-size:13px;line-height:15px;text-align:center;font-weight:700;box-shadow:2px 2px 3px rgba(0,0,0,.4);display:flex;flex-direction:column;justify-content:center}
.tab.quick{font-weight:400;font-size:12px;justify-content:flex-end;padding-bottom:6px}

.footer{left:0;top:1111px;width:1043px;height:89px;background:var(--red)}
.flink{top:1129px;font-size:14px;color:var(--white);border-bottom:1px dotted var(--white)}
.flink::before{content:"› ";font-weight:700}
.social{top:1121px;width:33px;height:32px;border-radius:5px}
.copyright{left:0;top:1178px;width:1043px;text-align:center;font-size:12px;color:var(--white)}
</style>
</head>
<body>

<header>
  <div class="abs topbar">
    <span class="call">
      <svg width="16" height="16" viewBox="0 0 24 24" aria-hidden="true"><path fill="#fff" d="M6.6 10.8a15 15 0 0 0 6.6 6.6l2.2-2.2a1 1 0 0 1 1-.25 11 11 0 0 0 3.6.6 1 1 0 0 1 1 1V20a1 1 0 0 1-1 1A17 17 0 0 1 3 4a1 1 0 0 1 1-1h3.5a1 1 0 0 1 1 1 11 11 0 0 0 .6 3.6 1 1 0 0 1-.25 1z"/></svg>
      Make a Reservation : (02) 4700 5182
    </span>
  </div>
  <div class="abs brandband"></div>
  <div class="abs brand">
    <span class="mark"></span>
    <span class="name">Golden Lantern</span>
  </div>
  <nav class="abs mainnav">
    <a style="left:261px">Home</a>
    <a style="left:364px">Menu</a>
    <a style="left:469px">Gallery</a>
    <a style="left:574px">Contact</a>
    <a style="left:683px">Reservations</a>
  </nav>
  <div class="abs rule grey"></div>
  <div class="abs rule pink1"></div>
</header>

<section>
  <div class="abs hero" role="img" aria-label="Close-up photo of golden fried dishes"></div>
  <div class="abs hero-shade"></div>
  <h1 class="abs hero-title">Contact Us</h1>
  <div class="abs rule pink2"></div>
  <div class="abs rule pink3"></div>
</section>

<main>
  <div class="abs content"></div>

  <div class="abs map" role="img" aria-label="Street map showing the restaurant location"></div>
  <p class="abs address">Golden Lantern Chinese Restaurant<br>Shop 3, 8-12 Riverbend Street Kingsvale NSW 2750</p>
  <svg class="abs divider" viewBox="0 0 394 14" aria-hidden="true">
    <line x1="0" y1="3" x2="394" y2="3" stroke="#eee" stroke-width="1.5"/>
    <polygon points="367,3 379,3 373,12" fill="#fff"/>
  </svg>
  <p class="abs callout">For Reservation Please Call Us On
    <svg width="20" height="20" viewBox="0 0 24 24" style="vertical-align:-4px" aria-hidden="true"><circle cx="12" cy="12" r="10.5" fill="none" stroke="#f2df8a" stroke-width="2"/><path fill="#f2df8a" d="M9 7.5l1.4 2.5-1 1a6 6 0 0 0 3.6 3.6l1-1 2.5 1.4-.6 1.8c-4 .3-8-3.7-7.7-7.7z"/></svg>
    <span class="phone">(02) 4700 5182</span><br>or Use The Form Below</p>

  <span class="abs label" style="top:737px">Name »</span>
  <div class="abs field" style="top:762px;width:256px;height:28px"></div>
  <span class="abs label" style="top:811px">Email »</span>
  <div class="abs field" style="top:836px;width:256px;height:28px"></div>
  <span class="abs label" style="top:885px">Message »</span>
  <div class="abs field" style="top:910px;width:393px;height:129px"></div>
  <div class="abs submit">Submit</div>

  <aside>
    <div class="abs side"></div>
    <div class="abs side-head" style="top:422px">Opening Hours</div>
    <span class="abs meal" style="top:456px">LUNCH</span>
    <div class="abs hours-row lunch" style="top:476px;border:none"><span class="day">Monday- Friday</span><span class="time">11:30am - 3:00pm</span></div>
    <span class="abs meal" style="top:505px">DINNER</span>
    <div class="abs hours-row" style="top:526px"><span class="day">Monday</span><span class="time"><svg width="14" height="14" viewBox="0 0 14 14"><circle cx="7" cy="7" r="6" fill="none" stroke="#222" stroke-width="1.3"/><path d="M7 3.5V7l2.5 1.5" fill="none" stroke="#222" stroke-width="1.3"/></svg>5:00pm - 9:30pm</span></div>
    <div class="abs hours-row" style="top:550px"><span class="day">Tuesday</span><span class="time"><svg width="14" height="14" viewBox="0 0 14 14"><circle cx="7" cy="7" r="6" fill="none" stroke="#222" stroke-width="1.3"/><path d="M7 3.5V7l2.5 1.5" fill="none" stroke="#222" stroke-width="1.3"/></svg>5:00pm - 9:30pm</span></div>
    <div class="abs hours-row" style="top:575px"><span class="day">Wednesday</span><span class="time"><svg width="14" height="14" viewBox="0 0 14 14"><circle cx="7" cy="7" r="6" fill="none" stroke="#222" stroke-width="1.3"/><path d="M7 3.5V7l2.5 1.5" fill="none" stroke="#222" stroke-width="1.3"/></svg>5:00pm - 9:30pm</span></div>
    <div class="abs hours-row" style="top:600px"><span class="day">Thursday</span><span class="time"><svg width="14" height="14" viewBox="0 0 14 14"><circle cx="7" cy="7" r="6" fill="none" stroke="#222" stroke-width="1.3"/><path d="M7 3.5V7l2.5 1.5" fill="none" stroke="#222" stroke-width="1.3"/></svg>5:00pm - 9:30pm</span></div>
    <div class="abs hours-row" style="top:625px"><span class="day">Friday</span><span class="time"><svg width="14" height="14" viewBox="0 0 14 14"><circle cx="7" cy="7" r="6" fill="none" stroke="#222" stroke-width="1.3"/><path d="M7 3.5V7l2.5 1.5" fill="none" stroke="#222" stroke-width="1.3"/></svg>5:00pm - 10:30pm</span></div>
    <div class="abs hours-row" style="top:649px"><span class="day">Saturday</span><span class="time"><svg width="14" height="14" viewBox="0 0 14 14"><circle cx="7" cy="7" r="6" fill="none" stroke="#222" stroke-width="1.3"/><path d="M7 3.5V7l2.5 1.5" fill="none" stroke="#222" stroke-width="1.3"/></svg>5:00pm - 10:30pm</span></div>
    <div class="abs hours-row" style="top:674px"><span class="day">Sunday</span><span class="time"><svg width="14" height="14" viewBox="0 0 14 14"><circle cx="7" cy="7" r="6" fill="none" stroke="#222" stroke-width="1.3"/><path d="M7 3.5V7l2.5 1.5" fill="none" stroke="#222" stroke-width="1.3"/></svg>5:00pm - 10:30pm</span></div>
    <div class="abs hours-row" style="top:699px;border:none"><span class="day">Public Holiday</span><span class="time"><svg width="14" height="14" viewBox="0 0 14 14"><circle cx="7" cy="7" r="6" fill="none" stroke="#222" stroke-width="1.3"/><path d="M7 3.5V7l2.5 1.5" fill="none" stroke="#222" stroke-width="1.3"/></svg>5:00pm - 9:30pm</span></div>
    <div class="abs dash"></div>

    <div class="abs side-head" style="top:745px">Mouth-Watering Recipes</div>
    <span class="abs recipe" style="top:785px">ORANGE HONEY RIBS</span>
    <span class="abs recipe" style="top:803px">SEAFOOD SUPREME</span>
    <span class="abs recipe" style="top:821px">SOYA SOFT NOODLES</span>
    <span class="abs recipe" style="top:839px">GANG KEOWAN (MEAT)</span>
    <span class="abs recipe" style="top:857px">MONGOLIAN LAMB</span>
    <span class="abs recipe" style="top:875px">SHUN TUNG CHICKEN</span>
  </aside>

  <div class="abs tab" style="top:542px;height:44px">Bussiness<br>lunch</div>
  <div class="abs tab" style="top:600px;height:44px">Take Away<br>Menu</div>
  <div class="abs tab quick" style="top:736px;height:90px">
    <svg width="48" height="48" viewBox="0 0 48 48" style="margin:0 auto 4px" aria-hidden="true"><circle cx="24" cy="24" r="22" fill="#fff"/><circle cx="24" cy="24" r="22" fill="none" stroke="#e5433f" stroke-width="3"/><rect x="15" y="10" width="19" height="28" rx="2" fill="#d9a545"/><path d="M18 17h13M18 21h13M18 25h13M18 29h9" stroke="#fff" stroke-width="1.4"/></svg>
    Quick<br>Reservation</div>
</main>

<footer>
  <div class="abs footer"></div>
  <span class="abs flink" style="left:198px">Contact Us</span>
  <span class="abs flink" style="left:297px">About Us</span>
  <span class="abs social" style="left:652px;background:#2d4f96"></span>
  <span class="abs social" style="left:690px;background:#2aa3e0"></span>
  <span class="abs social" style="left:729px;background:#b31c24"></span>
  <span class="abs social" style="left:768px;background:#f08a1c"></span>
  <p class="abs copyright">Copyright © 2013, GoldenLantern.com, All Rights Reserved.</p>
</footer>

</body>
</html>
```